Brivora Collective Business Card Design

We need a business card design for Brivora Collective. We are a healthcare recruiting, wellness and education company. We partner with medical facilities to find quality candidates. We also offer free wellness courses.
The final design should communicate an emphasis on recruiting and wellness
The main purpose of the business card is to utilized it for networking events, give to hospitals, executives, VCs surgery centers and clinics. I want it to be sleek, clean, use of our brand colors and professional.

```html
<!DOCTYPE html>
<html lang="en">
<head>
<meta charset="utf-8">
<title>Brivora Collective Business Card</title>
<link href="https://fonts.googleapis.com/css2?family=Fira+Sans:wght@400;600&display=swap" rel="stylesheet">
<style>
  :root {
    --backdrop: #e6e6e6;
    --brand-teal: #025b53;
    --ink-light: #ffffff;
  }
  html, body {
    margin: 0;
    padding: 0;
    width: 1200px;
    height: 1200px;
    overflow: hidden;
    background: var(--backdrop);
    font-family: "Fira Sans", sans-serif;
  }
  .canvas {
    position: relative;
    width: 1200px;
    height: 1200px;
  }
  .card {
    position: absolute;
    left: 225px;
    width: 750px;
    height: 429px;
    background: var(--brand-teal);
    color: var(--ink-light);
  }
  .card--front { top: 152px; }
  .card--back { top: 619px; }

  .holder-name {
    position: absolute;
    top: 76px;
    left: 0;
    width: 100%;
    text-align: center;
    margin: 0;
    font-weight: 600;
    font-size: 61px;
    line-height: 1;
    letter-spacing: 0.5px;
  }
  .holder-position {
    position: absolute;
    top: 140px;
    left: 0;
    width: 100%;
    text-align: center;
    margin: 0;
    font-weight: 400;
    font-size: 41px;
    line-height: 1;
    letter-spacing: 0.5px;
  }
  .contact-item {
    position: absolute;
    display: flex;
    align-items: center;
    gap: 9px;
    font-size: 22px;
    letter-spacing: 0.6px;
    white-space: nowrap;
  }
  .contact-icon {
    width: 32px;
    height: 32px;
    background: var(--ink-light);
    display: flex;
    align-items: center;
    justify-content: center;
    flex: none;
  }
  .contact-icon svg { width: 24px; height: 24px; }
  .contact-item--phone { left: 101px; top: 249px; }
  .contact-item--email { left: 303px; top: 249px; }
  .contact-item--web { left: 127px; top: 312px; gap: 14px; }
  .contact-item--address { left: 388px; top: 312px; gap: 11px; }
  .contact-item--address .contact-text { padding-top: 6px; }

  .brand-lockup {
    position: absolute;
    left: 0;
    top: 0;
    width: 100%;
    height: 100%;
    display: flex;
    align-items: center;
    justify-content: center;
    gap: 22px;
  }
  .brand-mark {
    width: 62px;
    height: 62px;
    background: var(--ink-light);
    border-radius: 8px;
  }
  .brand-name {
    font-weight: 400;
    font-size: 48px;
    letter-spacing: 0.5px;
    line-height: 1;
  }
</style>
</head>
<body>
<main class="canvas">
  <section class="card card--front">
    <h1 class="holder-name">YOUR NAME</h1>
    <p class="holder-position">Your Position</p>

    <div class="contact-item contact-item--phone">
      <span class="contact-icon">
        <svg viewBox="0 0 24 24" aria-hidden="true">
          <path fill="#025b53" d="M6.6 3.5c.6-.4 1.4-.2 1.7.4l1.3 2.4c.3.6.1 1.2-.4 1.6l-.9.6c.6 1.9 2.1 3.9 3.9 5l.8-.8c.5-.5 1.2-.5 1.7-.2l2.2 1.6c.6.4.6 1.2.2 1.7l-1 1.2c-.7.8-2 1-3 .4C9 15.4 5.9 11.4 5.2 7.4c-.2-1.1.3-2.2 1.4-3.9z"/>
        </svg>
      </span>
      <span class="contact-text">000-000-0000</span>
    </div>

    <div class="contact-item contact-item--email">
      <span class="contact-icon">
        <svg viewBox="0 0 24 24" aria-hidden="true">
          <rect x="3" y="5" width="18" height="14" rx="2" fill="none" stroke="#025b53" stroke-width="2"/>
          <path d="M6 8l6 6 6-6" fill="none" stroke="#025b53" stroke-width="2"/>
        </svg>
      </span>
      <span class="contact-text">yourinformation@mailbox.com</span>
    </div>

    <div class="contact-item contact-item--web">
      <span class="contact-icon">
        <svg viewBox="0 0 24 24" aria-hidden="true">
          <g fill="none" stroke="#025b53" stroke-width="1.4">
            <circle cx="12" cy="12" r="9"/>
            <ellipse cx="12" cy="12" rx="4" ry="9"/>
            <line x1="12" y1="3" x2="12" y2="21"/>
            <line x1="3" y1="12" x2="21" y2="12"/>
            <line x1="4.5" y1="8" x2="19.5" y2="8"/>
            <line x1="4.5" y1="16" x2="19.5" y2="16"/>
          </g>
        </svg>
      </span>
      <span class="contact-text">wwyourinform.com</span>
    </div>

    <div class="contact-item contact-item--address">
      <span class="contact-icon">
        <svg viewBox="0 0 24 24" aria-hidden="true">
          <path fill="#025b53" d="M12 2a7 7 0 0 0-7 7c0 4.5 5 10.5 6.2 12a1 1 0 0 0 1.6 0C14 19.5 19 13.5 19 9a7 7 0 0 0-7-7z"/>
          <circle cx="12" cy="9" r="2.6" fill="#ffffff"/>
          <circle cx="12" cy="9" r="1.2" fill="#025b53"/>
        </svg>
      </span>
      <span class="contact-text">Your Address Here</span>
    </div>
  </section>

  <section class="card card--back">
    <div class="brand-lockup">
      <span class="brand-mark" aria-hidden="true"></span>
      <span class="brand-name">Brivora Collective</span>
    </div>
  </section>
</main>
</body>
</html>
```